Unique door chain needs a blister card design

We need a blister card design , card is 3.5 inches x 7.0 inches, limit to four colors, a unique and incredibly strong door chain that is also a flip lock, and can be installed in under a minute. Design should be simple and strong like the door chain. Based in los Angeles the company is bramblegate bolts. Bramblegatebolts.com

Target Market(s)

Home, apartment ,dorm room security

Industry/Entity Type

It Company

Font styles to use
Serif
Sans Serif

Requirements
Must have
• website address ,viewer can contact for home security tips and install tips. device name BRAMBLE GATE BOLT. Instructions for install and use of lock.

```html
<!DOCTYPE html>
<html lang="en">
<head>
<meta charset="utf-8">
<title>Bramble Gate Bolts – Blister Card</title>
<link rel="stylesheet" href="https://fonts.googleapis.com/css2?family=EB+Garamond:wght@400;500&display=swap">
<style>
  :root {
    --card-teal: #163d4d;
    --ink-white: #ffffff;
    --product-tone: #3a3f44;
    --product-light: #8a8f93;
  }
  html, body {
    margin: 0;
    padding: 0;
    width: 1200px;
    height: 2400px;
    overflow: hidden;
    background: var(--card-teal);
  }
  .card {
    position: relative;
    width: 1200px;
    height: 2400px;
    background: var(--card-teal);
    color: var(--ink-white);
    font-family: "EB Garamond", "Palatino Linotype", serif;
    overflow: hidden;
  }
  .hang-hole {
    position: absolute;
    left: 450px;
    top: 100px;
    width: 300px;
    height: 84px;
    border-radius: 50%;
    background: var(--ink-white);
  }
  .brand-spine {
    position: absolute;
    left: 20px;
    top: 0;
    width: 210px;
    height: 2400px;
    display: flex;
    align-items: center;
    justify-content: center;
  }
  .brand-spine span {
    writing-mode: vertical-rl;
    transform: rotate(180deg);
    font-size: 198px;
    font-weight: 400;
    letter-spacing: 8px;
    line-height: 1;
    white-space: nowrap;
  }
  .content {
    position: absolute;
    left: 250px;
    width: 950px;
    margin: 0;
    text-align: center;
    font-weight: 400;
  }
  .headline {
    top: 332px;
    font-size: 81px;
    line-height: 1.2;
  }
  .fit-claim {
    top: 592px;
    font-size: 80px;
    line-height: 1.2;
  }
  .product-shot {
    position: absolute;
    left: 380px;
    top: 930px;
    width: 720px;
    height: 220px;
    border-radius: 24px;
    background: linear-gradient(90deg, var(--product-tone) 0%, var(--product-tone) 65%, var(--product-light) 100%);
  }
  .instructions {
    top: 1340px;
  }
  .instructions h2 {
    margin: 0;
    font-size: 56px;
    font-weight: 400;
    line-height: 1.1;
  }
  .instructions p {
    margin: 0;
    font-size: 35px;
    line-height: 1.34;
  }
  .install-note {
    top: 1834px;
    font-size: 54px;
    line-height: 1.4;
  }
  .website {
    top: 2030px;
    font-size: 40px;
    line-height: 1.2;
    letter-spacing: 1px;
  }
  .product-name {
    top: 2130px;
    font-size: 83px;
    line-height: 1.2;
  }
</style>
</head>
<body>
  <main class="card">
    <div class="hang-hole"></div>

    <div class="brand-spine"><span>BRAMBLE GATE BOLTS</span></div>

    <h1 class="content headline">THE STRONGEST &amp;<br>SIMPLEST TO INSTALL</h1>

    <p class="content fit-claim">FITS ALL TYPES OF<br>DOOR HANDLES</p>

    <div class="product-shot" role="img" aria-label="Product photo of the door chain and flip lock with its key-ring style loop"></div>

    <section class="content instructions">
      <h2>INSTRUCTIONS</h2>
      <p>REMOVE THE TWO SCREWS HOLDING YOUR<br>
      CURRENT STRIKE PLATE (LOCATED NEXT TO<br>
      DOOR HANDLE ON DOOR FRAME), AND INSTALL<br>
      THE BRAMBLE GATE BOLT WITH THE TWO ENCLOSED<br>
      SCREWS. TO SECURE DOOR WHEN CLOSED SWING<br>
      THE FLIP LOCK TO THE CLOSED POSITION.<br>
      TO SECURE THE DOOR WHEN IT IS OPEN PLACE<br>
      THE LARGE RING OVER THE DOOR HANDLE.</p>
    </section>

    <p class="content install-note">INSTALL IN ONE MINUTE USING<br>A PHILLIPS SCREWDRIVER</p>

    <p class="content website">BRAMBLEGATEBOLTS.COM</p>

    <p class="content product-name">DOOR CHAIN &amp;<br>FLIP LOCK</p>
  </main>
</body>
</html>
```